BRISK GUARD WEBSITE BANNER DESIGN OF AWESOME

Please take a look at the attached Banner. I want a redesign Idea. The requirements are below.

1)Must Use Website Background
2)Must Use Photo Provided
3)Must Include Button
4)Website the banner will be used on you can see the current at the bottom of the page: https://b.plomvarn.com

Target Market(s)

Anyone Seeking Security Guard Services

```html
<!DOCTYPE html>
<html lang="en">
<head>
<meta charset="utf-8">
<title>Brisk Guard – Website Banner Options</title>
<link href="https://fonts.googleapis.com/css2?family=Poppins:wght@400;500;600;700&display=swap" rel="stylesheet">
<style>
  :root {
    --page-bg: #ffffff;
    --banner-blue: #1b4e77;
    --banner-blue-light: #21567f;
    --banner-blue-deep: #1f3c68;
    --accent-gold: #fbab1d;
    --text-white: #ffffff;
    --button-text: #1d4d78;
    --photo-dark: #121a26;
    --photo-mid: #2a3c58;
    --photo-light: #6f8fb8;
  }
  * { margin: 0; padding: 0; box-sizing: border-box; }
  html, body {
    width: 1200px; height: 868px; overflow: hidden;
    background: var(--page-bg);
    font-family: "Poppins", sans-serif;
  }
  .canvas { position: relative; width: 1200px; height: 868px; }
  .banner {
    position: absolute; left: 71px; width: 1058px; height: 343px;
    overflow: hidden; background: var(--banner-blue);
  }
  .banner--chevron { top: 64px; }
  .banner--fade { top: 461px; }
  .banner-backdrop { position: absolute; inset: 0; width: 100%; height: 100%; }
  .banner-photo {
    position: absolute; inset: 0; width: 100%; height: 100%;
  }
  .banner-copy {
    position: absolute; left: 70px; top: 70px; color: var(--text-white);
  }
  .headline {
    font-weight: 600; font-size: 44px; line-height: 1; letter-spacing: 0.2px;
  }
  .tagline {
    margin-top: 10px; font-weight: 500; font-size: 22px; line-height: 1;
  }
  .feature-list {
    list-style: none; display: flex; gap: 14px; margin-top: 26px;
    font-size: 15px; line-height: 1;
  }
  .feature-list li { display: flex; align-items: center; gap: 5px; }
  .feature-list svg { width: 18px; height: 17px; }
  .cta-button {
    position: absolute; left: 66px; top: 224px;
    width: 179px; height: 41px; border-radius: 21px;
    background: var(--accent-gold); color: var(--button-text);
    display: flex; align-items: center; justify-content: center; gap: 5px;
    font-weight: 600; font-size: 16px; text-decoration: none;
  }
  .cta-button svg { width: 15px; height: 15px; }
</style>
</head>
<body>
<div class="canvas">

  <section class="banner banner--chevron">
    <svg class="banner-backdrop" viewBox="0 0 1058 343" preserveAspectRatio="none" aria-hidden="true">
      <polygon points="0,0 420,0 0,150" fill="var(--banner-blue-light)" opacity="0.5"/>
      <polygon points="0,230 560,150 600,343 0,343" fill="var(--banner-blue-light)" opacity="0.35"/>
      <polygon points="330,343 1058,150 1058,343" fill="var(--banner-blue-deep)"/>
    </svg>
    <svg class="banner-photo" viewBox="0 0 1058 343" preserveAspectRatio="none" role="img" aria-label="Photo: security guard in a uniform jacket shining a flashlight up a dark stairwell">
      <defs>
        <linearGradient id="photoToneA" x1="0" y1="0" x2="1" y2="0.3">
          <stop offset="0" stop-color="var(--photo-dark)"/>
          <stop offset="0.55" stop-color="var(--photo-mid)"/>
          <stop offset="1" stop-color="var(--photo-light)"/>
        </linearGradient>
      </defs>
      <polygon points="519,0 545,0 591,171 545,343 519,343 583,171" fill="var(--accent-gold)"/>
      <polygon points="545,0 1058,0 1058,343 545,343 591,171" fill="url(#photoToneA)"/>
    </svg>
    <div class="banner-copy">
      <h1 class="headline">Get Secured Today</h1>
      <p class="tagline">We take your security personal.</p>
      <ul class="feature-list">
        <li><svg viewBox="0 0 18 17"><rect x="1" y="4" width="12" height="12" fill="none" stroke="var(--accent-gold)" stroke-width="1.6"/><path d="M4 9l3 3 9-11" fill="none" stroke="var(--accent-gold)" stroke-width="1.8"/></svg>Client Portal</li>
        <li><svg viewBox="0 0 18 17"><rect x="1" y="4" width="12" height="12" fill="none" stroke="var(--accent-gold)" stroke-width="1.6"/><path d="M4 9l3 3 9-11" fill="none" stroke="var(--accent-gold)" stroke-width="1.8"/></svg>24x7 Dispatch</li>
        <li><svg viewBox="0 0 18 17"><rect x="1" y="4" width="12" height="12" fill="none" stroke="var(--accent-gold)" stroke-width="1.6"/><path d="M4 9l3 3 9-11" fill="none" stroke="var(--accent-gold)" stroke-width="1.8"/></svg>No Binding Contracts</li>
      </ul>
    </div>
    <a class="cta-button" href="https://b.plomvarn.com">GET STARTED
      <svg viewBox="0 0 16 16"><circle cx="8" cy="8" r="8" fill="var(--button-text)"/><path d="M4 8h7M8 4.5L11.5 8 8 11.5" fill="none" stroke="var(--accent-gold)" stroke-width="2"/></svg>
    </a>
  </section>

  <section class="banner banner--fade">
    <svg class="banner-backdrop" viewBox="0 0 1058 343" preserveAspectRatio="none" aria-hidden="true">
      <polygon points="0,0 420,0 0,150" fill="var(--banner-blue-light)" opacity="0.5"/>
      <polygon points="0,230 560,150 600,343 0,343" fill="var(--banner-blue-light)" opacity="0.35"/>
      <polygon points="330,343 1058,150 1058,343" fill="var(--banner-blue-deep)"/>
    </svg>
    <svg class="banner-photo" viewBox="0 0 1058 343" preserveAspectRatio="none" role="img" aria-label="Photo: security guard in a uniform jacket shining a flashlight up a dark stairwell, fading into the blue background">
      <defs>
        <linearGradient id="photoToneB" x1="0" y1="0" x2="1" y2="0">
          <stop offset="0" stop-color="var(--photo-dark)" stop-opacity="0"/>
          <stop offset="0.35" stop-color="var(--photo-dark)" stop-opacity="0.7"/>
          <stop offset="0.7" stop-color="var(--photo-mid)"/>
          <stop offset="1" stop-color="var(--photo-light)"/>
        </linearGradient>
      </defs>
      <rect x="560" y="0" width="498" height="343" fill="url(#photoToneB)"/>
    </svg>
    <div class="banner-copy">
      <h2 class="headline">Get Secured Today</h2>
      <p class="tagline">We take your security personal.</p>
      <ul class="feature-list">
        <li><svg viewBox="0 0 18 17"><rect x="1" y="4" width="12" height="12" fill="none" stroke="var(--accent-gold)" stroke-width="1.6"/><path d="M4 9l3 3 9-11" fill="none" stroke="var(--accent-gold)" stroke-width="1.8"/></svg>Client Portal</li>
        <li><svg viewBox="0 0 18 17"><rect x="1" y="4" width="12" height="12" fill="none" stroke="var(--accent-gold)" stroke-width="1.6"/><path d="M4 9l3 3 9-11" fill="none" stroke="var(--accent-gold)" stroke-width="1.8"/></svg>24x7 Dispatch</li>
        <li><svg viewBox="0 0 18 17"><rect x="1" y="4" width="12" height="12" fill="none" stroke="var(--accent-gold)" stroke-width="1.6"/><path d="M4 9l3 3 9-11" fill="none" stroke="var(--accent-gold)" stroke-width="1.8"/></svg>No Binding Contracts</li>
      </ul>
    </div>
    <a class="cta-button" href="https://b.plomvarn.com">GET STARTED
      <svg viewBox="0 0 16 16"><circle cx="8" cy="8" r="8" fill="var(--button-text)"/><path d="M4 8h7M8 4.5L11.5 8 8 11.5" fill="none" stroke="var(--accent-gold)" stroke-width="2"/></svg>
    </a>
  </section>

</div>
</body>
</html>
```